K.T.L Electrical Services Pty Ltd

Electrical contracting business. I have a base for the design which i like. The contact number needs to be changed to 0491736250 and the O made more solid and level with the rest of the letters. If you have any other ideas of what would make it better I'm happy to see them.

The back side to be written as dot points with the following:
- Residential & Commercial
- Maintenance
- PV & Battery servicing
- EV Chargers

```html
<!DOCTYPE html>
<html lang="en">
<head>
<meta charset="utf-8">
<title>K.T.L Electrical Services – Business Card</title>
<link rel="stylesheet" href="https://fonts.googleapis.com/css2?family=Roboto:wght@400;500;700&display=swap">
<style>
  :root {
    --page: #3a3b3d;
    --card: #1d1f22;
    --blue: #1f7df0;
    --blue-bright: #1a9bf5;
    --white: #f2f4f7;
  }
  * { box-sizing: border-box; margin: 0; padding: 0; }
  html, body { width: 1200px; height: 694px; overflow: hidden; }
  body {
    background: var(--page);
    font-family: "Roboto", Arial, sans-serif;
    position: relative;
  }
  .card {
    position: absolute;
    top: 190px;
    width: 540px;
    height: 310px;
    background: var(--card);
    border-radius: 24px;
    box-shadow: 0 7px 0 var(--blue), 0 18px 30px rgba(0,0,0,0.45);
    overflow: hidden;
  }
  .card--front { left: 40px; }
  .card--back { left: 620px; }

  /* Brand block */
  .brand { display: flex; align-items: center; gap: 16px; }
  .brand__dot { border-radius: 50%; background: var(--blue); flex: none; }
  .brand__text { color: var(--blue-bright); font-weight: 500; line-height: 1; }
  .brand__initials { display: block; letter-spacing: 2px; }
  .brand__full { display: block; letter-spacing: 1.5px; text-transform: uppercase; }
  .brand__licence { color: var(--blue); font-weight: 500; letter-spacing: 1px; }

  .card--front .brand { position: absolute; left: 80px; top: 92px; }
  .card--front .brand__dot { width: 96px; height: 96px; }
  .card--front .brand__initials { font-size: 72px; }
  .card--front .brand__full { font-size: 19px; margin-top: 8px; }
  .card--front .brand__licence { position: absolute; right: 70px; top: 214px; font-size: 16px; }

  .card--back .brand { position: absolute; right: 34px; top: 30px; gap: 10px; }
  .card--back .brand__dot { width: 44px; height: 44px; }
  .card--back .brand__initials { font-size: 34px; }
  .card--back .brand__full { font-size: 9.5px; margin-top: 4px; }
  .card--back .brand__licence { position: absolute; right: 36px; top: 92px; font-size: 9px; }

  .person { position: absolute; left: 34px; top: 108px; }
  .person__name { color: var(--blue-bright); font-size: 26px; font-weight: 500; }
  .person__role { color: var(--white); font-size: 10px; font-weight: 500; letter-spacing: 1px; text-transform: uppercase; }

  .services { position: absolute; left: 34px; top: 162px; }
  .services__title { color: var(--blue); font-size: 20px; font-weight: 500; letter-spacing: 1px; margin-bottom: 6px; }
  .services__list { list-style: none; color: var(--white); font-size: 15px; line-height: 1.5; }
  .services__list li::before {
    content: ""; display: inline-block; width: 7px; height: 7px; border-radius: 50%;
    background: var(--blue); margin-right: 9px; vertical-align: middle;
  }
  .services__list--right { position: absolute; left: 300px; top: 122px; }

  .phone { position: absolute; left: 34px; bottom: 20px; display: flex; align-items: center; gap: 12px; }
  .phone__number { color: var(--white); font-size: 30px; font-weight: 700; letter-spacing: 1px; }

  .email-band {
    position: absolute; right: 0; bottom: 0; width: 250px; height: 58px;
    background: var(--blue); border-top-left-radius: 20px;
    display: flex; align-items: center; gap: 8px; padding-left: 22px;
    color: var(--white); font-size: 13px;
  }
</style>
</head>
<body>
  <section class="card card--front" aria-label="Card front">
    <div class="brand">
      <span class="brand__dot"></span>
      <span class="brand__text">
        <span class="brand__initials">K.T.L</span>
        <span class="brand__full">Electrical Services P/L</span>
      </span>
    </div>
    <span class="brand__licence">EC 20418</span>
  </section>

  <section class="card card--back" aria-label="Card back">
    <div class="brand">
      <span class="brand__dot"></span>
      <span class="brand__text">
        <span class="brand__initials">K.T.L</span>
        <span class="brand__full">Electrical Services P/L</span>
      </span>
    </div>
    <span class="brand__licence">EC 20418</span>

    <div class="person">
      <p class="person__name">Liam Hartwell</p>
      <p class="person__role">Your Position</p>
    </div>

    <div class="services">
      <p class="services__title">OUR SERVICES</p>
      <ul class="services__list">
        <li>Residential &amp; Commercial</li>
        <li>Maintenance</li>
      </ul>
    </div>
    <ul class="services__list services__list--right">
      <li>PV &amp; Battery servicing</li>
      <li>EV Chargers</li>
    </ul>

    <div class="phone">
      <svg width="28" height="28" viewBox="0 0 24 24" aria-hidden="true">
        <path fill="#1f7df0" d="M6.6 10.8a15.1 15.1 0 0 0 6.6 6.6l2.2-2.2c.3-.3.7-.4 1-.2 1.1.4 2.3.6 3.6.6.6 0 1 .4 1 1V20c0 .6-.4 1-1 1A17 17 0 0 1 3 4c0-.6.4-1 1-1h3.5c.6 0 1 .4 1 1 0 1.3.2 2.5.6 3.6.1.3 0 .7-.2 1z"/>
      </svg>
      <span class="phone__number">0491736250</span>
    </div>

    <div class="email-band">
      <svg width="16" height="12" viewBox="0 0 16 12" aria-hidden="true">
        <rect x="0.5" y="0.5" width="15" height="11" rx="1" fill="#f2f4f7"/>
        <path d="M1 1l7 5.5L15 1" fill="none" stroke="#1f7df0" stroke-width="1.3"/>
      </svg>
      <span>info@ktlelectrical.com</span>
    </div>
  </section>
</body>
</html>
```